Facebook Header Design Project.

I'm supplying white and colored logos. The Facebook page already exists. URL = https://www.pagebook.example/lumocrest.design The design should not be based on what's already there. Consider mobile implications of the design. This Design will form the designs of other social media headers. LumoCrest is a web design | digital marketing company.

Target Market(s)

People interested in web design | digital marketing services.

Industry/Entity Type

LumoCrest is a web design | digital marketing company. That should be clear in the design.

Colors
0054AA
0677BA
7BADD7
CADEEF
E8F1F8

Requirements
Must have
• Logo. Use Facebook header image dimension.
Nice to have
• Use a color scheme like the logo and feel free to add a color or two from the other side of the color whee.

```html
<!DOCTYPE html>
<html lang="en">
<head>
<meta charset="UTF-8">
<title>LumoCrest – Web Design &amp; Digital Marketing Header</title>
<link rel="stylesheet" href="https://fonts.googleapis.com/css2?family=Bebas+Neue&family=Source+Sans+3:wght@600;700&display=swap">
<style>
  :root {
    --stage: #0b1a3a;
    --white: #ffffff;
    --brand-deep: #0054AA;
    --brand-mid: #0677BA;
    --brand-soft: #7BADD7;
    --brand-pale: #CADEEF;
    --brand-mist: #E8F1F8;
    --headline: #24519a;
    --icon-ink: #0e2a5a;
    --scene-lavender: #eef0f8;
    --scene-lilac: #dfe3f1;
    --scene-blue: #4f7fd6;
    --scene-teal: #6cc9bd;
    --scene-coral: #e07a72;
  }
  * { margin: 0; padding: 0; box-sizing: border-box; }
  html, body {
    width: 1200px;
    height: 744px;
    overflow: hidden;
    background: var(--stage);
  }
  .header-banner {
    position: absolute;
    left: 67px;
    top: 174px;
    width: 1066px;
    height: 396px;
    background: var(--white);
    border-radius: 3px;
    overflow: hidden;
    font-family: "Source Sans 3", Arial, sans-serif;
  }
  .brand-name {
    position: absolute;
    left: 58px;
    top: 28px;
    font-weight: 700;
    font-size: 40px;
    line-height: 1;
    color: var(--brand-deep);
  }
  .social-links {
    position: absolute;
    left: 863px;
    top: 20px;
    display: flex;
    gap: 38px;
    list-style: none;
  }
  .social-links li {
    width: 15px;
    height: 15px;
    border-radius: 50%;
    background: var(--icon-ink);
  }
  .accent-grid-top {
    position: absolute;
    left: 452px;
    top: 59px;
    width: 48px;
    height: 48px;
    background: var(--brand-mist);
    border-radius: 4px;
  }
  .accent-grid-left {
    position: absolute;
    left: 10px;
    top: 260px;
    width: 74px;
    height: 39px;
    background: var(--brand-mist);
    border-radius: 4px;
  }
  .headline-glow {
    position: absolute;
    left: 0;
    top: 94px;
    width: 175px;
    height: 151px;
    background: linear-gradient(90deg, var(--brand-soft) 0%, var(--brand-pale) 45%, rgba(255,255,255,0) 100%);
    opacity: 0.8;
  }
  .headline {
    font-family: "Bebas Neue", Impact, sans-serif;
    font-weight: 400;
  }
  .headline-primary,
  .headline-secondary {
    position: absolute;
    left: 57px;
    line-height: 1;
    white-space: nowrap;
  }
  .headline-primary {
    top: 98px;
    font-size: 70px;
    letter-spacing: 4px;
    color: var(--headline);
    -webkit-text-stroke: 1.5px var(--headline);
  }
  .headline-secondary {
    top: 163px;
    font-size: 82px;
    letter-spacing: 1px;
    color: transparent;
    -webkit-text-stroke: 2px var(--brand-mid);
  }
  .intro-band {
    position: absolute;
    left: 0;
    top: 311px;
    width: 720px;
    height: 85px;
    background: linear-gradient(90deg, var(--brand-mid) 0%, #2b8fc8 35%, var(--brand-pale) 70%, rgba(255,255,255,0) 100%);
  }
  .intro-text {
    position: absolute;
    left: 55px;
    top: 326px;
    width: 390px;
    font-size: 12.5px;
    font-weight: 600;
    line-height: 17px;
    color: var(--white);
  }
  .workspace-illustration {
    position: absolute;
    left: 629px;
    top: 44px;
    width: 437px;
    height: 352px;
    border-radius: 70px 14px 0 0;
    background:
      radial-gradient(ellipse 110px 120px at 62% 62%, rgba(79,127,214,0.55), rgba(79,127,214,0) 100%),
      radial-gradient(ellipse 80px 60px at 20% 78%, rgba(108,201,189,0.6), rgba(108,201,189,0) 100%),
      radial-gradient(ellipse 50px 70px at 90% 60%, rgba(108,201,189,0.45), rgba(108,201,189,0) 100%),
      radial-gradient(ellipse 60px 30px at 80% 92%, rgba(224,122,114,0.5), rgba(224,122,114,0) 100%),
      linear-gradient(160deg, var(--scene-lavender) 0%, var(--scene-lilac) 100%);
  }
</style>
</head>
<body>
  <section class="header-banner">
    <div class="brand-name">LumoCrest</div>

    <ul class="social-links" aria-label="Social channels">
      <li aria-label="Social channel"></li>
      <li aria-label="Social channel"></li>
      <li aria-label="Social channel"></li>
      <li aria-label="Social channel"></li>
    </ul>

    <div class="accent-grid-top" role="img" aria-label="Small decorative plus-sign grid"></div>

    <div class="headline-glow"></div>
    <h1 class="headline">
      <span class="headline-primary">Web Design &amp;</span>
      <span class="headline-secondary">Digital Marketing</span>
    </h1>

    <div class="accent-grid-left" role="img" aria-label="Small decorative dot grid"></div>

    <div class="intro-band"></div>
    <p class="intro-text">LumoCrest builds fast, modern websites and runs digital marketing campaigns that help growing businesses get found, win trust and turn visitors into customers.</p>

    <div class="workspace-illustration" role="img" aria-label="Illustration of a woman working at a desk with a laptop, notebook, plant, lamp and framed pictures"></div>
  </section>
</body>
</html>
```